Mobile Product Filter for Luxury footwear e-commerce store

We would like to see designs for a "Mobile First" product filter for our collection pages:
http://shop.quillarven.example/collections/mukluks

The design should have a high degree of mobile usability and fit with the current look & feel.

Filtering options would be:

- Category: Mukluks / Moccasins / Puddlestep / Accessories
- Size: 5,6,7,8,9,10,11,12,13
- Gender: Male / Female / Unisex / Kids
- Color: Ideally show color swatches otherwise color names (Tan / Stone / Black / Cocoa /Tobacco / Russet)
- Sole: Korlex / Crepe / Leather
- Materials: Fur / Faux Fur / No Fur
- Production: Made in Canada / International
- Price: Up to $100 / $100 to $500 / $500 and more
- In Stock: Yes / No

** Sorting Options**
- Most Popular
- Highest Rates
- Price: High to Low
- Price: Low to High

BONUS POINTS: Provide the desktop view as well.

Target Market(s)

Women

Industry/Entity Type

E-Commerce

Number of Pages Required

2 page

Font styles to use
Sans Serif

Requirements
Must have
• Mobile first design
Nice to have
• Desktop design

```html
<!DOCTYPE html>
<html lang="en">
<head>
<meta charset="utf-8">
<title>Quillarven Mukluks – Collection Filter</title>
<link rel="stylesheet" href="https://fonts.googleapis.com/css2?family=Mulish:wght@400;600;700;800&display=swap">
<style>
  :root {
    --ink: #222222;
    --muted: #8a8a8a;
    --header: #000000;
    --field-bg: #efefef;
    --field-line: #c9c9c9;
    --radio-line: #c4c4c4;
    --accent: #e5371e;
    --price-red: #e8261b;
    --track: #555555;
    --panel-line: #c8c8c8;
    --chat: #3a3a3a;
    --white: #ffffff;
  }
  * { box-sizing: border-box; margin: 0; padding: 0; }
  html, body { width: 676px; height: 1200px; overflow: hidden; background: var(--white); }
  body { position: relative; font-family: "Mulish", sans-serif; color: var(--ink); }

  .site-header { position: absolute; left: 0; top: 0; width: 676px; height: 116px; background: var(--header); }
  .brand { position: absolute; left: 34px; top: 30px; color: var(--white); font-weight: 800; font-size: 38px; letter-spacing: 2px; line-height: 1; }
  .brand-sub { display: block; font-size: 17px; letter-spacing: 12px; margin-top: 6px; padding-left: 64px; font-weight: 800; }
  .menu-toggle { position: absolute; left: 602px; top: 38px; width: 38px; height: 38px; }

  .filter-label { position: absolute; right: 526px; font-size: 19px; color: var(--ink); text-align: right; white-space: nowrap; transform: translateY(-50%); }
  .select { position: absolute; left: 187px; width: 455px; height: 50px; background: var(--field-bg); border: 1px solid var(--field-line); font-size: 16px; color: var(--muted); padding: 0 12px; display: flex; align-items: center; }
  .select::after { content: ""; position: absolute; right: 18px; top: 22px; border-left: 7px solid transparent; border-right: 7px solid transparent; border-top: 5px solid #444; }

  .options { position: absolute; left: 187px; display: flex; align-items: center; transform: translateY(-50%); }
  .option { display: flex; align-items: center; font-size: 16px; color: var(--muted); margin-right: 13px; }
  .option::before { content: ""; width: 26px; height: 26px; border: 1.5px solid var(--radio-line); border-radius: 50%; margin-right: 15px; }

  .sorting { position: absolute; left: 33px; top: 784px; width: 609px; height: 280px; border: 1px solid var(--panel-line); border-radius: 2px; }
  .sorting-title { position: absolute; left: 24px; top: 16px; font-size: 19px; font-weight: 600; }
  .sort-label { position: absolute; right: 440px; font-size: 16px; white-space: nowrap; transform: translateY(-50%); }
  .sort-label small { font-size: 13px; }
  .sort-input { position: absolute; left: 200px; width: 383px; height: 37px; border: 1px solid var(--field-line); background: var(--white); }
  .range { position: absolute; left: 200px; width: 383px; height: 8px; background: var(--track); border-radius: 4px; }
  .range::before { content: ""; position: absolute; left: 9px; top: -7px; width: 20px; height: 20px; border-radius: 50%; background: var(--white); border: 2px solid var(--price-red); }
  .range-values { position: absolute; left: 200px; width: 383px; display: flex; justify-content: space-between; font-size: 14px; }
  .range-values b { font-weight: 400; color: var(--price-red); }

  .search-btn { position: absolute; left: 32px; top: 1077px; width: 610px; height: 45px; background: var(--accent); color: var(--white); font-size: 19px; letter-spacing: 0.5px; display: flex; align-items: center; justify-content: center; border-radius: 2px; }

  .chat-bar { position: absolute; left: 32px; top: 1137px; width: 612px; height: 70px; background: var(--chat); border: 2px solid #222; border-radius: 14px 14px 0 0; color: var(--white); }
  .chat-bar span { position: absolute; left: 32px; top: 18px; font-size: 27px; font-weight: 700; }
  .chat-bar svg { position: absolute; right: 30px; top: 24px; }
</style>
</head>
<body>
  <header class="site-header">
    <div class="brand">QUILLARVEN<span class="brand-sub">MUKLUKS</span></div>
    <svg class="menu-toggle" viewBox="0 0 38 38" aria-label="Menu">
      <rect x="0" y="3" width="38" height="4" fill="#fff"/>
      <rect x="0" y="17" width="38" height="4" fill="#fff"/>
      <rect x="0" y="31" width="38" height="4" fill="#fff"/>
    </svg>
  </header>

  <main class="filters">
    <div class="filter-label" style="top:166px">Categories</div>
    <div class="select" style="top:142px">Mukluks</div>

    <div class="filter-label" style="top:226px">Size</div>
    <div class="select" style="top:202px">Select Size</div>

    <div class="filter-label" style="top:284px">Gender</div>
    <div class="options" style="top:285px">
      <span class="option">Male</span><span class="option">Female</span><span class="option">Unisex</span><span class="option">Kids</span>
    </div>

    <div class="filter-label" style="top:331px">Color</div>
    <div class="options" style="top:332px">
      <span class="option">Tan</span><span class="option">Stone</span><span class="option">Black</span><span class="option">Cocoa</span>
    </div>
    <div class="options" style="top:377px">
      <span class="option">Tobacco</span><span class="option">Russet</span>
    </div>

    <div class="filter-label" style="top:438px">Sole</div>
    <div class="select" style="top:414px">Select Sole</div>

    <div class="filter-label" style="top:498px">Materials</div>
    <div class="select" style="top:474px">Select Materials</div>

    <div class="filter-label" style="top:558px">Production</div>
    <div class="options" style="top:558px">
      <span class="option">Made in Canada</span><span class="option">International</span>
    </div>

    <div class="filter-label" style="top:612px">Price</div>
    <div class="select" style="top:587px">Select Price</div>

    <div class="filter-label" style="top:669px">In Stock</div>
    <div class="options" style="top:669px">
      <span class="option" style="margin-right:30px">Yes</span><span class="option">No</span>
    </div>

    <section class="sorting">
      <div class="sorting-title">Sorting Options</div>

      <div class="sort-label" style="top:74px">Most Popular</div>
      <div class="sort-input" style="top:55px"></div>

      <div class="sort-label" style="top:119px">Highest Rates</div>
      <div class="sort-input" style="top:101px"></div>

      <div class="sort-label" style="top:165px">Price <small>( High to Low )</small></div>
      <div class="range" style="top:162px"></div>
      <div class="range-values" style="top:178px"><span>High- <b>$000.00</b></span><span>Low- <b>$00.00</b></span></div>

      <div class="sort-label" style="top:224px">Price <small>( Low to High )</small></div>
      <div class="range" style="top:221px"></div>
      <div class="range-values" style="top:237px"><span>Low- <b>$00.00</b></span><span>High- <b>$000.00</b></span></div>
    </section>

    <div class="search-btn">SEARCH NOW ››</div>
  </main>

  <div class="chat-bar">
    <span>Leave a message</span>
    <svg width="34" height="22" viewBox="0 0 34 22" aria-label="Expand">
      <polyline points="3,19 17,5 31,19" fill="none" stroke="#fff" stroke-width="6"/>
    </svg>
  </div>
</body>
</html>
```